5x5 Pop Up Display, Company Logo With Text and Graphics for Tradeshow Display

Design for a 5ft x 5ft pop up trade show display that will sit on top of a table. I usually prefer clean, somewhat minimalist designs. We are a food service company but it's not a requirement to have photos of food. Design elements should compliment the table cloth that we have for the booth. The below may be included depending on the design aesthetic.
Service Provided: Daily Meal Service, Kitchen Management
"Nationwide Footprint"
"Grassroots Service"
"Fresh Scratch Cooking"
"Custom Menus"
"Made To Order Meals"

```html
<!DOCTYPE html>
<html lang="en">
<head>
<meta charset="utf-8">
<title>Hearthside Kitchens – 5x5 Tabletop Display</title>
<link rel="stylesheet" href="https://fonts.googleapis.com/css2?family=Quicksand:wght@500;700&family=Saira+Semi+Condensed:wght@500;600&display=swap">
<style>
  :root {
    --charcoal: #1f1f1f;
    --charcoal-soft: #2b2b2b;
    --lime: #b8dc2c;
    --leaf: #7fb321;
    --white: #ffffff;
    --map-green: #5f8a45;
    --screen-grey: #e9ece6;
  }
  html, body {
    margin: 0;
    width: 1200px;
    height: 1200px;
    overflow: hidden;
    background: var(--white);
  }
  .display {
    position: relative;
    width: 1200px;
    height: 1200px;
    background: linear-gradient(180deg, var(--charcoal-soft) 0%, var(--charcoal) 100%);
    overflow: hidden;
    font-family: "Quicksand", sans-serif;
    color: var(--white);
  }
  .food-backdrop {
    position: absolute;
    left: 60px; top: 80px;
    width: 1080px; height: 760px;
    border-radius: 50%;
    background: radial-gradient(ellipse at center, rgba(90,90,90,0.35) 0%, rgba(60,60,60,0.2) 55%, rgba(40,40,40,0) 75%);
  }
  .frame {
    position: absolute;
    inset: 42px;
    border: 3px solid var(--lime);
  }
  .brand {
    position: absolute;
    top: 210px; left: 0; right: 0;
    display: flex;
    justify-content: center;
    align-items: center;
    gap: 26px;
  }
  .brand-name {
    font-family: "Quicksand", sans-serif;
    font-weight: 700;
    font-size: 104px;
    line-height: 0.95;
    text-align: center;
    color: var(--white);
    letter-spacing: 1px;
  }
  .brand-dot {
    width: 46px; height: 46px;
    border-radius: 50%;
    background: var(--leaf);
  }
  .tagline {
    position: absolute;
    top: 580px; left: 0; right: 0;
    margin: 0;
    height: 60px;
    line-height: 60px;
    text-align: center;
    font-family: "Saira Semi Condensed", sans-serif;
    font-weight: 500;
    font-size: 48px;
    letter-spacing: 1px;
    text-transform: uppercase;
    white-space: nowrap;
  }
  .tagline .accent { color: var(--leaf); font-weight: 600; }
  .tagline-rule {
    position: absolute;
    top: 664px; left: 490px;
    width: 220px; height: 4px;
    background: var(--lime);
  }
  .feature {
    position: absolute;
    top: 740px;
    width: 340px;
    text-align: center;
  }
  .feature-daily { left: 200px; }
  .feature-nationwide { left: 660px; }
  .feature-art { display: block; margin: 0 auto; height: 210px; }
  .feature-label {
    margin-top: 22px;
    font-size: 44px;
    line-height: 1.08;
    font-weight: 500;
  }
  .feature-label .accent {
    display: block;
    font-family: "Saira Semi Condensed", sans-serif;
    font-weight: 600;
    color: var(--leaf);
  }
</style>
</head>
<body>
<main class="display">
  <div class="food-backdrop" role="img" aria-label="Faint dark photograph of a fresh grilled meal"></div>
  <div class="frame"></div>

  <header class="brand">
    <div class="brand-name">Hearthside<br>Kitchens</div>
    <div class="brand-dot"></div>
  </header>

  <p class="tagline">Fresh Scratch <span class="accent">Cooking</span></p>
  <div class="tagline-rule"></div>

  <section class="feature feature-daily">
    <svg class="feature-art" width="90" height="210" viewBox="0 0 90 210" role="img" aria-label="Phone showing the meal ordering app">
      <rect x="2" y="2" width="86" height="206" rx="12" fill="#111" stroke="#555" stroke-width="2"/>
      <rect x="8" y="12" width="74" height="186" rx="6" fill="var(--screen-grey)"/>
      <rect x="8" y="12" width="74" height="20" rx="6" fill="#3f6a30"/>
    </svg>
    <div class="feature-label">Daily Meal<span class="accent">Service</span></div>
  </section>

  <section class="feature feature-nationwide">
    <svg class="feature-art" width="230" height="210" viewBox="0 0 230 210" role="img" aria-label="Illustrated map of the United States with service team members">
      <rect x="10" y="20" width="210" height="150" rx="30" fill="var(--map-green)"/>
    </svg>
    <div class="feature-label">Nationwide<span class="accent">Footprint</span></div>
  </section>
</main>
</body>
</html>
```